I am looking for a stand-out cover that sings out to new parents. The category is very pastel with limited compelling covers that would make me want to buy a book. This book will be used often in the first 12 months of baby's life - so must be strong enough to sit on the bedside table or on the coffee table to inspire reading. It will be a popular gift - so needs to look credible, "pick-up-able" and loveable.

The Book Title is - The Little Sprout Handbook on an Infant's Opening Months: Gentle, Research-Backed Methods for Rest, Nourishment, Protection and Growing Assurance
The Size is - 8.5 x 11 in
Book description to be provided to final design for inclusion
Some examples of book covers in this category attached. Thanks

```html
<!DOCTYPE html>
<html lang="en">
<head>
<meta charset="utf-8">
<title>The Little Sprout Handbook – Cover</title>
<link rel="stylesheet" href="https://fonts.googleapis.com/css2?family=Allura&family=Cinzel:wght@400;600;700&display=swap">
<style>
  :root{
    --stage:#ffffff;
    --paper:#ffffff;
    --teal:#5b93a3;
    --teal-deep:#4f8696;
    --coral:#f28a82;
    --sun:#f3c65e;
    --sun-pale:#f7dfa0;
    --cream:#fdf3d8;
    --white:#ffffff;
    --stripe:#eceef0;
  }
  *{margin:0;padding:0;box-sizing:border-box}
  html,body{width:1200px;height:574px;overflow:hidden;background:var(--stage)}
  .stage{position:relative;width:1200px;height:574px}
  .cover{
    position:absolute;left:399px;top:27px;width:402px;height:520px;
    background:var(--paper);overflow:hidden;
    box-shadow:0 4px 14px rgba(0,0,0,.18);
  }
  .cover__stripes{position:absolute;left:55px;top:0;width:40px;height:40px;
    background:repeating-linear-gradient(90deg,var(--stripe) 0 6px,transparent 6px 11px);opacity:.8}
  .cover__arch{
    position:absolute;left:0;top:40px;width:402px;height:480px;
    border-radius:201px 201px 0 0;
    background:radial-gradient(ellipse at 50% 45%,#6aa0b0 0%,var(--teal) 55%,var(--teal-deep) 100%);
  }
  .cover__glow{position:absolute;border-radius:50%;filter:blur(6px)}
  .cover__glow--sun{left:292px;top:30px;width:80px;height:84px;background:var(--sun-pale);opacity:.85;border-radius:45% 55% 40% 60%}
  .cover__glow--heart{left:360px;top:112px;width:44px;height:40px;background:var(--coral);opacity:.8;filter:blur(3px)}
  .cover__spine-band{
    position:absolute;left:24px;top:0;width:26px;height:497px;
    background:var(--sun);border-radius:0 0 13px 13px;
    display:flex;align-items:center;justify-content:center;
  }
  .cover__spine-text{
    writing-mode:vertical-rl;transform:rotate(180deg);
    font-family:'Cinzel',serif;font-size:17.5px;letter-spacing:.5px;color:var(--cream);white-space:nowrap;
  }
  .cover__emblem{
    position:absolute;left:117px;top:0;width:169px;height:119px;
    background:var(--coral);border-radius:0 0 85px 85px;
  }
  .cover__title{
    position:absolute;left:50px;right:45px;top:138px;text-align:center;color:var(--white);
  }
  .title__script{font-family:'Allura',cursive;font-size:32px;line-height:1;color:var(--white)}
  .title__hero{font-family:'Cinzel',serif;font-weight:600;font-size:44px;line-height:.95;color:var(--sun);letter-spacing:1px}
  .title__bridge{font-family:'Cinzel',serif;font-size:17px;line-height:1.2;letter-spacing:.5px}
  .title__focus{display:flex;justify-content:center;align-items:center;gap:5px;color:var(--coral);font-family:'Cinzel',serif}
  .title__focus-main{font-size:38px;font-weight:600;line-height:1}
  .title__focus-stack{font-size:14px;line-height:1;text-align:left}
  .cover__subtitle{
    position:absolute;left:50px;right:40px;top:282px;text-align:center;
    font-family:'Cinzel',serif;font-weight:700;font-size:9px;line-height:1.35;color:var(--white);letter-spacing:.2px;
  }
  .cover__photo{
    position:absolute;left:69px;top:311px;width:243px;height:209px;
    border-radius:121px 121px 0 0;
    background:linear-gradient(160deg,#f4ece6 0%,#d9b79c 40%,#a77c5c 65%,#f1ebe6 100%);
  }
  .cover__topics{position:absolute;left:331px;top:206px;width:52px;height:314px}
  .topics__line{position:absolute;left:25.5px;top:0;width:1px;height:314px;background:var(--white);opacity:.85}
  .topics__dot{position:absolute;left:0;width:52px;height:52px;border-radius:50%;display:flex;align-items:center;justify-content:center}
  .topics__dot--rest{top:117px;background:var(--coral)}
  .topics__dot--feed{top:178px;background:var(--sun)}
  .topics__dot--safe{top:239px;background:var(--white)}
</style>
</head>
<body>
<main class="stage">
  <article class="cover">
    <div class="cover__stripes"></div>
    <div class="cover__arch" role="img" aria-label="Soft teal photograph of cupped parent hands holding a baby's feet"></div>
    <div class="cover__glow cover__glow--sun" role="img" aria-label="Soft blurred yellow heart decoration"></div>
    <div class="cover__glow cover__glow--heart" role="img" aria-label="Soft blurred coral heart decoration"></div>

    <div class="cover__spine-band">
      <span class="cover__spine-text">Baby Guide&nbsp;&nbsp;&nbsp;Baby Guide&nbsp;&nbsp;&nbsp;Baby Guide</span>
    </div>

    <div class="cover__emblem" role="img" aria-label="White line illustration of a sleeping newborn"></div>

    <h1 class="cover__title">
      <div class="title__script">The Little</div>
      <div class="title__hero">SPROUT</div>
      <div class="title__bridge">HANDBOOK ON AN</div>
      <div class="title__focus">
        <span class="title__focus-main">INFANT'S</span>
        <span class="title__focus-stack">OPENING<br>MONTHS</span>
      </div>
    </h1>

    <p class="cover__subtitle">Gentle, Research-Backed Methods for Rest,<br>Nourishment, Protection and Growing Assurance</p>

    <div class="cover__photo" role="img" aria-label="Photograph of a smiling mother lying beside her baby on white bedding"></div>

    <div class="cover__topics">
      <div class="topics__line"></div>
      <div class="topics__dot topics__dot--rest">
        <svg width="24" height="24" viewBox="0 0 24 24" fill="none" stroke="#fff" stroke-width="1.4" stroke-linecap="round" stroke-linejoin="round" aria-label="Rest">
          <path d="M16 4a8 8 0 1 0 4 12A7 7 0 0 1 16 4z"/>
        </svg>
      </div>
      <div class="topics__dot topics__dot--feed">
        <svg width="24" height="24" viewBox="0 0 24 24" fill="none" stroke="#fff" stroke-width="1.4" stroke-linecap="round" stroke-linejoin="round" aria-label="Nourishment">
          <path d="M10 3h4v3h-4z"/><path d="M9 6h6l1 3v11a1 1 0 0 1-1 1H9a1 1 0 0 1-1-1V9z"/><path d="M8 12h8"/>
        </svg>
      </div>
      <div class="topics__dot topics__dot--safe">
        <svg width="24" height="24" viewBox="0 0 24 24" fill="none" stroke="#4f8696" stroke-width="1.4" stroke-linecap="round" stroke-linejoin="round" aria-label="Protection">
          <path d="M12 3l7 3v5c0 5-3 8-7 10-4-2-7-5-7-10V6z"/><path d="M9 12l2 2 4-4"/>
        </svg>
      </div>
    </div>
  </article>
</main>
</body>
</html>
```